Need a corporate background Image with our existing logo for Zoom or Microsoft Teams

Hi,

We require a corporate background image with our existing logo use with Zoom or Microsoft Teams.

Our existing logo is at https://www.halvenrock-systems.com/images/logo_top.png

Thank you.

```html
<!DOCTYPE html>
<html lang="en">
<head>
<meta charset="utf-8">
<title>Halvenrock Systems – Meeting Background</title>
<link href="https://fonts.googleapis.com/css2?family=Archivo:wght@700&display=swap" rel="stylesheet">
<style>
  :root {
    --deep-blue: #0a1f8c;
    --mid-blue: #0c45c8;
    --glow-blue: #1560e0;
    --bright-blue: #1f7cf0;
    --cyan: #22c8ee;
    --aqua: #34e0f0;
  }
  * { margin: 0; padding: 0; box-sizing: border-box; }
  html, body {
    width: 1200px;
    height: 681px;
    overflow: hidden;
  }
  .meeting-background {
    position: relative;
    width: 1200px;
    height: 681px;
    overflow: hidden;
    background:
      radial-gradient(ellipse 620px 420px at 590px 330px, var(--mid-blue) 0%, rgba(12,69,200,0) 100%),
      linear-gradient(135deg, #0b36b0 0%, var(--deep-blue) 100%);
  }
  .tech-cluster {
    position: absolute;
    inset: 0;
  }
  .tech-cluster--top-right {
    background:
      radial-gradient(ellipse 180px 120px at 1010px 70px, rgba(52,224,240,0.55) 0%, rgba(52,224,240,0) 100%),
      radial-gradient(ellipse 120px 90px at 1170px 350px, rgba(52,224,240,0.6) 0%, rgba(52,224,240,0) 100%),
      radial-gradient(ellipse 420px 300px at 1040px 110px, rgba(31,124,240,0.85) 0%, rgba(31,124,240,0) 100%);
  }
  .tech-cluster--bottom-left {
    background:
      radial-gradient(ellipse 140px 90px at 120px 641px, rgba(52,224,240,0.55) 0%, rgba(52,224,240,0) 100%),
      radial-gradient(ellipse 60px 60px at 0 361px, rgba(52,224,240,0.6) 0%, rgba(52,224,240,0) 100%),
      radial-gradient(ellipse 380px 250px at 150px 621px, rgba(31,124,240,0.85) 0%, rgba(31,124,240,0) 100%);
  }
  .brand {
    position: absolute;
    left: 68px;
    top: 76px;
    display: flex;
    align-items: center;
    gap: 18px;
  }
  .brand__mark {
    width: 58px;
    height: 58px;
    border-radius: 50%;
    background: var(--cyan);
  }
  .brand__name {
    font-family: "Archivo", Arial, sans-serif;
    font-weight: 700;
    font-size: 44px;
    letter-spacing: -0.5px;
    color: var(--cyan);
    line-height: 1;
    white-space: nowrap;
  }
</style>
</head>
<body>
  <main class="meeting-background">
    <div class="tech-cluster tech-cluster--top-right" role="img" aria-label="Cluster of glowing blue and cyan hexagons with circuit lines"></div>
    <div class="tech-cluster tech-cluster--bottom-left" role="img" aria-label="Cluster of glowing blue and cyan hexagons with circuit lines"></div>
    <div class="brand">
      <span class="brand__mark"></span>
      <span class="brand__name">Halvenrock Systems</span>
    </div>
  </main>
</body>
</html>
```